Stationery Design
Business Card, Envelopes and letterhead
Professional
Dwight Halloway
Production Manager
4172 N. Wrenfield Rd.
Baton Rouge LA 70913
dwight@velmorpack.com
www.velmorpack.com
Please propose letterhead, business card and envelope design using the new logo just uploaded

```html
<!DOCTYPE html>
<html lang="en">
<head>
<meta charset="utf-8">
<title>Velmor Packaging Works — Business Card</title>
<link rel="stylesheet" href="https://fonts.googleapis.com/css2?family=Oswald:wght@600&family=Open+Sans:wght@400;600&display=swap">
<style>
  :root {
    --stage: #e6e6e4;
    --card-light: #ffffff;
    --card-dark: #2a2a2a;
    --card-dark-edge: #1c1c1c;
    --brand-blue: #27a6de;
    --brand-blue-soft: #8fd3f1;
    --ink: #2b2b2b;
    --ink-soft: #6b6b6b;
    --on-dark: #f2f2f2;
  }
  * { box-sizing: border-box; margin: 0; padding: 0; }
  html, body { width: 1200px; height: 974px; overflow: hidden; }
  body {
    background: var(--stage);
    font-family: "Open Sans", Arial, sans-serif;
    position: relative;
  }
  .card {
    position: absolute;
    width: 620px;
    height: 354px;
    border-radius: 4px;
    box-shadow: 0 10px 30px rgba(0,0,0,.18);
    overflow: hidden;
  }
  .card--front { left: 500px; top: 90px; background: var(--card-light); }
  .card--back {
    left: 80px; top: 530px;
    background: radial-gradient(ellipse at 50% 45%, #3a3a3a 0%, var(--card-dark) 55%, var(--card-dark-edge) 100%);
  }
  .swoosh { position: absolute; inset: 0; }
  .brand {
    position: absolute;
    left: 0; right: 0;
    display: flex; flex-direction: column; align-items: center;
  }
  .brand__row { display: flex; align-items: center; gap: 10px; }
  .brand__dot { width: 14px; height: 14px; border-radius: 50%; background: var(--brand-blue); }
  .brand__name {
    font-family: "Oswald", Arial, sans-serif;
    font-weight: 600;
    letter-spacing: 2px;
    line-height: 1;
  }
  .brand__tagline {
    font-family: "Oswald", Arial, sans-serif;
    font-weight: 600;
    text-transform: uppercase;
    letter-spacing: .5px;
    margin-top: 6px;
  }
  .card--front .brand { top: 36px; }
  .card--front .brand__name { font-size: 52px; color: var(--ink); }
  .card--front .brand__tagline { font-size: 13px; color: var(--ink); }
  .card--back .brand { top: 110px; }
  .card--back .brand__name { font-size: 72px; color: var(--on-dark); }
  .card--back .brand__tagline { font-size: 17px; color: var(--on-dark); }

  .contact { position: absolute; left: 72px; top: 170px; color: var(--ink-soft); font-size: 11px; line-height: 1.55; }
  .contact__name { color: var(--brand-blue); font-size: 19px; font-weight: 600; line-height: 1.2; }
  .contact__title { font-size: 12px; margin-bottom: 10px; }
  .contact__label { color: var(--brand-blue); font-weight: 600; }
</style>
</head>
<body>

<section class="card card--front" aria-label="Business card, front">
  <svg class="swoosh" viewBox="0 0 620 354" aria-hidden="true">
    <path d="M250,0 H620 V175 C575,70 440,18 250,0 Z" fill="var(--brand-blue)"/>
    <path d="M300,0 C460,22 585,85 620,190 V175 C575,70 440,18 250,0 Z" fill="var(--brand-blue-soft)"/>
    <path d="M0,250 C70,310 170,340 300,354 H0 Z" fill="var(--brand-blue)"/>
    <path d="M0,240 C70,300 170,333 300,354 H280 C160,338 70,306 0,260 Z" fill="var(--brand-blue-soft)"/>
  </svg>
  <div class="brand">
    <div class="brand__row"><span class="brand__dot"></span><span class="brand__name">VPK</span></div>
    <div class="brand__tagline">Velmor Packaging Works</div>
  </div>
  <div class="contact">
    <div class="contact__name">Dwight Halloway</div>
    <div class="contact__title">Production Manager</div>
    <div>4172 N. Wrenfield Rd. Baton Rouge LA 70913</div>
    <div><span class="contact__label">Toll free :</span> 1-800-555-0142</div>
    <div><span class="contact__label">T:</span> 225 555 0187 | <span class="contact__label">F:</span> 225 555 0193 | <span class="contact__label">C:</span> 225 555 0176</div>
    <div><span class="contact__label">E:</span> dwight@velmorpack.com | <span class="contact__label">W:</span> www.velmorpack.com</div>
  </div>
</section>

<section class="card card--back" aria-label="Business card, back">
  <div class="brand">
    <div class="brand__row"><span class="brand__dot"></span><span class="brand__name">VPK</span></div>
    <div class="brand__tagline">Velmor Packaging Works</div>
  </div>
</section>

</body>
</html>
```